Business Intelligence Application - Reporting Menu and Report Criteria Design

Looking for a fresh, effective and user friendly view for the menu structure and reporting criteria screen format for a business reporting application. Initial format completed, content structure is in place, but we need the 'wow' design.. as its a serious professional report/BI tool it has to fall within certain guidelines for clarity and graphics..but we want it to be slick, friendly, great user experience. There is a large amount of complex content to fit into a small space and we need it to be very inviting, modern and intuitive.. If interested, please review the attachment. We have live screens in operation, but feel these could be improved and looking forward to seeing what great creative suggestions could be made. Please review work done to date in the attached.. We are not looking for a total re-design of everything, all the basic business content/structure is there.. but tell us what we could do to improve this in terms of graphic design... particularly the criteria screens.. thanks!
Updates

Reason: Need a few more days to review designs - thanks for all submissions so far, we will make a selection shortly.

Target Market(s)

Business analysts, hotel operations teams, finance analysts hospitality industry

Industry/Entity Type

Hospitality

Coding

Coded - Design and coding required

Number of Pages Required

4 page

Font styles to use
Sans Serif
Other font styles liked:
• Candara, please see example in deck

Colors
3276b5
3176b5
0255a3
85acd3
33a6d7
cee9f5
85cae6

Requirements
Must have
• sharp clear, logical menu structure, (currently it has 'clicks to sub-menus, we need hover over, slide to sub-menus..) colour, styling.. and most focus on revision of criteria.. right now is somewhat heavy, cumbersome.. keep colour and friendly intuitive process steps.. its heavy analytical stuff.. best of luck!
Should not have
• No grey fonts on white or grey screens! many business apps are not readable or sharp.. or fonts are too small.. colourless, so please avoid that.. see our deck - sharp dark (navy) or black fonts on white, or light shading..

```html
<!DOCTYPE html>
<html lang="en">
<head>
<meta charset="utf-8">
<title>Silver Crest Hotels &amp; Suites – Reporting</title>
<link href="https://fonts.googleapis.com/css2?family=Cabin:wght@400;500;600;700&display=swap" rel="stylesheet">
<style>
  :root {
    --navy: #0255a3;
    --sky: #33a6d7;
    --ink: #1a1f2b;
    --white: #ffffff;
    --line: #7f8a96;
    --divider: rgba(255,255,255,0.35);
    --dot: #3276b5;
  }
  * { box-sizing: border-box; margin: 0; padding: 0; }
  html, body { width: 1200px; height: 508px; overflow: hidden; background: var(--white); }
  body { position: relative; font-family: "Cabin", sans-serif; color: var(--ink); }

  .topbar { position: absolute; left: 0; top: 0; width: 1200px; height: 60px; background: var(--navy); color: var(--white); }
  .brand { position: absolute; left: 47px; top: 0; height: 60px; display: flex; align-items: center; gap: 10px; font-size: 19px; font-weight: 600; letter-spacing: -0.2px; }
  .brand-mark { width: 20px; height: 20px; border-radius: 50%; background: var(--white); }
  .welcome { position: absolute; left: 556px; top: 22px; font-size: 13.5px; }
  .date { position: absolute; left: 668px; top: 22px; font-size: 13.5px; }
  .top-button { position: absolute; top: 11px; width: 107px; height: 37px; background: var(--sky); color: var(--white); font-size: 12.5px; font-weight: 600; letter-spacing: 0.4px; display: flex; align-items: center; justify-content: center; }
  .top-button.intel { left: 834px; }
  .top-button.planning { left: 956px; }
  .icon-bell { position: absolute; left: 1084px; top: 17px; }
  .icon-exit { position: absolute; left: 1125px; top: 18px; }

  .section-nav { position: absolute; left: 47px; top: 89px; display: flex; align-items: center; font-size: 13px; font-weight: 600; color: var(--ink); }
  .section-nav .sep { width: 3px; height: 3px; border-radius: 50%; background: var(--dot); margin: 0 9px; }

  .property-search { position: absolute; left: 775px; top: 81px; width: 373px; height: 37px; border: 1px solid var(--line); display: flex; align-items: center; padding-left: 17px; font-size: 11.5px; color: var(--ink); letter-spacing: 0.2px; }
  .property-search svg { position: absolute; right: 10px; top: 11px; }

  .menu { position: absolute; list-style: none; font-size: 11.5px; color: var(--white); box-shadow: 0 2px 6px rgba(2,85,163,0.18); }
  .menu li { height: 33.6px; display: flex; align-items: center; padding-left: 11px; background: var(--sky); border-bottom: 1px solid var(--divider); position: relative; }
  .menu li:last-child { border-bottom: none; }
  .menu li.active { background: var(--navy); }
  .menu .caret { position: absolute; right: 11px; top: 13px; }
  .menu-main { left: 775px; top: 141px; width: 164px; }
  .menu-main li:last-child { height: 38px; }
  .menu-main::before { content: ""; position: absolute; left: 11px; top: -8px; border-left: 8px solid transparent; border-right: 8px solid transparent; border-bottom: 8px solid var(--navy); }
  .menu-names { left: 952px; top: 141px; width: 163px; }
  .menu-region { left: 952px; top: 242px; width: 163px; }
  .menu-region li { padding-left: 13px; }
  .menu-names li { padding-left: 13px; }
  .menu-hotels { left: 962px; top: 319px; width: 164px; }
  .menu-hotels li { padding-left: 13px; height: 34px; }
  .menu-hotels li:last-child { height: 37px; }
</style>
</head>
<body>
  <header class="topbar">
    <div class="brand"><span class="brand-mark"></span>Silver Crest Hotels &amp; Suites</div>
    <div class="welcome">Welcome Admin</div>
    <div class="date">Tuesday October 04.2017</div>
    <div class="top-button intel">INTEL</div>
    <div class="top-button planning">PLANNING</div>
    <svg class="icon-bell" width="26" height="24" viewBox="0 0 26 24" fill="none" stroke="#fff" stroke-width="1.4" stroke-linecap="round" stroke-linejoin="round" aria-label="Notifications">
      <path d="M8 17V11a5 5 0 0 1 10 0v6l2 2H6z"/>
      <path d="M11 21a2 2 0 0 0 4 0"/>
      <path d="M4 8a6 6 0 0 0 0 7M22 8a6 6 0 0 1 0 7"/>
      <path d="M13 4v2"/>
    </svg>
    <svg class="icon-exit" width="28" height="22" viewBox="0 0 28 22" fill="none" stroke="#fff" stroke-width="1.4" stroke-linejoin="round" aria-label="Sign out">
      <path d="M18 12v7H2V7h6"/>
      <path d="M6 16c2-6 7-8 13-8V4l7 6-7 6v-4c-5 0-9 1-13 4z"/>
    </svg>
  </header>

  <nav class="section-nav">
    <span>Admin</span><span class="sep"></span>
    <span>Management</span><span class="sep"></span>
    <span>Rooms Performance</span><span class="sep"></span>
    <span>Revenue Summary</span><span class="sep"></span>
    <span>Demand &amp; Risk</span><span class="sep"></span>
    <span>Inventory Analysis</span><span class="sep"></span>
    <span>Placeholder</span>
  </nav>

  <div class="property-search">PROPERTY SEARCH
    <svg width="15" height="15" viewBox="0 0 15 15" fill="none" stroke="#1a1f2b" stroke-width="1.3"><circle cx="6.5" cy="6.5" r="5"/><path d="M10.2 10.2l3.5 3.5" stroke-linecap="round"/></svg>
  </div>

  <ul class="menu menu-main">
    <li class="active">Property Name<svg class="caret" width="5" height="8" viewBox="0 0 5 8"><path d="M0 0l5 4-5 4z" fill="#fff"/></svg></li>
    <li>Property ID</li>
    <li>Product Type</li>
    <li class="active">Europe<svg class="caret" width="5" height="8" viewBox="0 0 5 8"><path d="M0 0l5 4-5 4z" fill="#fff"/></svg></li>
    <li>All Region</li>
    <li>All Area</li>
  </ul>

  <ul class="menu menu-names">
    <li>Regent Row Hotel</li>
    <li>Grand Regent Hotel</li>
  </ul>

  <ul class="menu menu-region">
    <li>UK &amp; Ireland</li>
    <li>Central London<svg class="caret" width="9" height="5" viewBox="0 0 9 5" style="top:15px"><path d="M0 0h9L4.5 5z" fill="#fff"/></svg></li>
  </ul>

  <ul class="menu menu-hotels">
    <li>Regent Row Hotel</li>
    <li>Grand Regent Hotel</li>
    <li>Southbank Quay Hotel</li>
    <li>Riverside Court Hotel</li>
  </ul>
</body>
</html>
```